its a new company based in Christchurch new Zealand building computers ,repairs, upgrades and anything computers for the general public,i like bright happy colours like yellows, greens reds anything that stands out and it needs to communicant trust and security towards my new company,i have no logo yet,

Target Market(s)

target market of all ages

Industry/Entity Type

Building

Contact Information for Business Card

Pixel Harbour Limited,ph-0274829315,email-brightnode47@mailvista.example,14c tamworth cl,kelvale

```html
<!DOCTYPE html>
<html lang="en">
<head>
<meta charset="utf-8">
<title>Pixel Harbour Limited – Business Card</title>
<link rel="stylesheet" href="https://fonts.googleapis.com/css2?family=Play:wght@400;700&display=swap">
<style>
  :root {
    --page-bg: #e4e6ea;
    --card-white: #ffffff;
    --card-shade: #f1f2f4;
    --brand-navy: #1f3f7a;
    --brand-red: #e53935;
    --brand-yellow: #f7c51e;
    --brand-yellow-soft: #fbe38a;
    --wave-top: #5cc24f;
    --wave-bottom: #1d7f36;
    --ink: #222428;
    --ink-light: #ffffff;
  }
  * { box-sizing: border-box; margin: 0; padding: 0; }
  html, body {
    width: 1200px;
    height: 900px;
    overflow: hidden;
    background: var(--page-bg);
    font-family: "Play", sans-serif;
  }
  .canvas { position: relative; width: 1200px; height: 900px; }

  .card {
    position: absolute;
    left: 250px;
    width: 700px;
    height: 400px;
    border-radius: 40px;
    overflow: hidden;
    background: linear-gradient(180deg, var(--card-white) 0%, var(--card-shade) 100%);
    box-shadow: 0 10px 26px rgba(0, 0, 0, 0.18);
  }
  .card--front { top: 35px; }
  .card--back { top: 465px; }

  .card__wave { position: absolute; inset: 0; width: 100%; height: 100%; }

  .brand {
    position: absolute;
    display: flex;
    align-items: center;
    gap: 12px;
    color: var(--brand-navy);
    font-weight: 700;
  }
  .brand__mark {
    width: 22px;
    height: 22px;
    background: var(--brand-red);
    flex: none;
  }
  .card--front .brand { left: 44px; top: 46px; font-size: 27px; }
  .card--back .brand {
    left: 0; right: 0; top: 0; bottom: 0;
    justify-content: center;
    font-size: 44px;
  }
  .card--back .brand__mark { width: 34px; height: 34px; }

  .person {
    position: absolute;
    right: 44px;
    top: 96px;
    text-align: right;
  }
  .person__name {
    color: var(--brand-red);
    font-size: 25px;
    letter-spacing: 0.5px;
    font-weight: 400;
  }
  .person__role {
    color: var(--ink);
    font-size: 17px;
    margin-top: 2px;
  }

  .contact {
    position: absolute;
    right: 40px;
    bottom: 28px;
    list-style: none;
    color: var(--ink-light);
    text-align: right;
    font-size: 15px;
    line-height: 1.2;
  }
  .contact__address { margin-bottom: 14px; font-size: 16px; }
  .contact__item {
    display: flex;
    justify-content: flex-end;
    align-items: center;
    gap: 10px;
    margin-top: 7px;
  }
  .contact__icon { width: 14px; height: 14px; flex: none; fill: var(--brand-yellow); }
</style>
</head>
<body>
<main class="canvas">

  <section class="card card--front" aria-label="Business card front">
    <svg class="card__wave" viewBox="0 0 700 400" preserveAspectRatio="none" aria-hidden="true">
      <defs>
        <linearGradient id="waveFill" x1="0" y1="0" x2="0" y2="1">
          <stop offset="0" stop-color="var(--wave-top)"/>
          <stop offset="1" stop-color="var(--wave-bottom)"/>
        </linearGradient>
      </defs>
      <path d="M0 150 C 170 120, 300 250, 470 220 C 580 200, 650 178, 700 182"
            fill="none" stroke="var(--brand-red)" stroke-width="3"/>
      <path d="M0 166 C 170 136, 300 268, 470 236 C 580 216, 650 194, 700 197"
            fill="none" stroke="var(--brand-yellow)" stroke-width="10"/>
      <path d="M0 190 C 170 160, 300 292, 470 258 C 580 236, 650 212, 700 214 L700 400 L0 400 Z"
            fill="url(#waveFill)"/>
      <path d="M0 200 C 170 172, 300 302, 470 268 C 580 246, 650 222, 700 224"
            fill="none" stroke="var(--brand-yellow-soft)" stroke-width="2" opacity="0.8"/>
    </svg>

    <div class="brand">
      <span class="brand__mark"></span>
      <span class="brand__name">Pixel Harbour Limited</span>
    </div>

    <div class="person">
      <h1 class="person__name">MARTIN HOLLOWAY</h1>
      <p class="person__role">Managing Director</p>
    </div>

    <ul class="contact">
      <li class="contact__address">14c Tamworth Cl,<br>Kelvale</li>
      <li class="contact__item">
        <span>027 482 9315</span>
        <svg class="contact__icon" viewBox="0 0 16 16" aria-label="Phone"><path d="M4 1 L6.5 1 L7.5 5 L5.5 6.5 C6.5 8.5 7.5 9.5 9.5 10.5 L11 8.5 L15 9.5 L15 12 C15 13.5 13.5 15 12 15 C6 15 1 10 1 4 C1 2.5 2.5 1 4 1 Z"/></svg>
      </li>
      <li class="contact__item">
        <span>brightnode47@mailvista.example</span>
        <svg class="contact__icon" viewBox="0 0 16 16" aria-label="Email"><path d="M1 3 H15 V13 H1 Z M2 4 L8 9 L14 4 Z" fill-rule="evenodd"/></svg>
      </li>
    </ul>
  </section>

  <section class="card card--back" aria-label="Business card back">
    <div class="brand">
      <span class="brand__mark"></span>
      <span class="brand__name">Pixel Harbour Limited</span>
    </div>
  </section>

</main>
</body>
</html>
```